Clothing range for the petite modern mature woman needs a card design

We need a business card design for a new Sydney based company called lark reed. We provide clothing to the modern mature woman who finds it difficult to source clothes that do not make them look frumpy or do not fit. We have an idea we would like an apple with the peel unravelling and possibly the silhouette of a woman's body coming out of the peel. The lark reed represents the womans body shape and dressing it.

Target Market(s)

modern mature aged woman

Industry/Entity Type

Clothing

Contact Information for Business Card

abn: 41270386915
will provide email at a later date
a spiel re clothes for modern woman???

Font styles to use
Serif
Sans Serif

Requirements
Must have
• will need name - ABN -will need email address but still working on that (TBA)
Nice to have
• picture of an apple with its peel coming off and possibly the silhouette of a woman coming out. the issue a lot of women in the over 50 range have is that the clothing is very dated or makes the woman frumpy. we are providing clothes for the woman who has difficulty in finding fashionable clothes in their size.
Should not have
• don't want childlike

```html
<!DOCTYPE html>
<html lang="en">
<head>
<meta charset="utf-8">
<title>Lark Reed – Business Card</title>
<link rel="stylesheet" href="https://fonts.googleapis.com/css2?family=Bodoni+Moda:wght@500&family=Arimo:wght@400&display=swap">
<style>
  :root {
    --backdrop: #ececec;
    --card-white: #ffffff;
    --brand-red: #c52b28;
    --brand-red-deep: #852429;
    --ink-grey: #5b5b5b;
    --ink-soft: #8c8c8c;
    --on-red: #ffffff;
  }
  * { margin: 0; padding: 0; box-sizing: border-box; }
  html, body {
    width: 1200px;
    height: 999px;
    overflow: hidden;
    background: var(--backdrop);
  }
  .stage {
    position: relative;
    width: 1200px;
    height: 999px;
  }
  .card {
    position: absolute;
    top: 158px;
    width: 399px;
    height: 660px;
  }
  .card--front {
    left: 177px;
    background: var(--card-white);
  }
  .card--back {
    left: 625px;
    background: var(--brand-red);
    color: var(--on-red);
    font-family: "Arimo", Arial, sans-serif;
  }
  .brand-dot {
    position: absolute;
    left: 164px;
    top: 252px;
    width: 70px;
    height: 70px;
    border-radius: 50%;
    background: var(--brand-red);
  }
  .brand-name {
    position: absolute;
    left: 0;
    width: 100%;
    top: 424px;
    text-align: center;
    font-family: "Bodoni Moda", "Didot", serif;
    font-weight: 500;
    font-size: 35px;
    letter-spacing: 1px;
    line-height: 1;
    color: var(--ink-grey);
  }
  .brand-tagline {
    position: absolute;
    left: 0;
    width: 100%;
    top: 460px;
    text-align: center;
    font-family: "Arimo", Arial, sans-serif;
    font-size: 15px;
    line-height: 1;
    color: var(--ink-soft);
  }
  .holder-bar {
    position: absolute;
    left: 0;
    top: 282px;
    width: 176px;
    height: 24px;
    background: var(--brand-red-deep);
  }
  .holder-name {
    position: absolute;
    left: 70px;
    top: 283px;
    font-size: 20px;
    line-height: 22px;
  }
  .contact-line {
    position: absolute;
    left: 69px;
    font-size: 16px;
    line-height: 1;
    letter-spacing: 0.2px;
  }
  .contact-line--mobile { top: 325px; }
  .contact-line--email { top: 358px; }
  .abn {
    position: absolute;
    right: 13px;
    top: 633px;
    font-size: 15px;
    line-height: 1;
  }
</style>
</head>
<body>
<main class="stage">
  <section class="card card--front">
    <div class="brand-dot"></div>
    <h1 class="brand-name">LARK REED</h1>
    <p class="brand-tagline">weekend collection for petite women</p>
  </section>

  <section class="card card--back">
    <div class="holder-bar"></div>
    <p class="holder-name">Mara Quell</p>
    <p class="contact-line contact-line--mobile">m . 0412 738 259</p>
    <p class="contact-line contact-line--email">e &nbsp;. larkreedpetite@mailnest.com</p>
    <p class="abn">abn: 41270386915</p>
  </section>
</main>
</body>
</html>
```